Wildlfower Field Guide Needs a Book Cover Design

We need a book cover design in formats compatible with Adobe Illustrator and/or Photoshop (vector file that can be edited). I have attached a Power Point file with the general design features for the front and back covers and photographs to be used in the book cover. The cover size is 6" wide by 9" high (same size as the attached Power Point file). The book cover should have the same format including photos as the attached file with a similar color scheme. We are looking for a sky blue background then title text in a complementary darker blue. The other color elements (borders around photos) can be the same darker blue or dark gray. We are looking for better text types/styles for the title than those is the attached file. All three lines of the title should have the same width (1st line - thicker text, 2nd line - white italics on dark background, 3rd line - narrow text). The dark background on the 2nd line would ideally have some texture or style like a trail. On the back cover, written paragraphs should remain in Ebrima font.

Requirements
Must have
• Project should follow general cover outline of attached Power Point file
• Should have desired color scheme
• Must include all photos as formatted in the attached in the Power point file
Nice to have
• The title (2nd line) can be a solid color matching 1st line text or texture like a hiking trail

```html
<!DOCTYPE html>
<html lang="en">
<head>
<meta charset="utf-8">
<title>Bloom Guide Beside the path – Book Cover</title>
<link href="https://fonts.googleapis.com/css2?family=Open+Sans:wght@400;700;800&family=Dancing+Script:wght@600&display=swap" rel="stylesheet">
<style>
  :root {
    --sky: #c9def0;
    --title-blue: #1c6db3;
    --band: #2a78bd;
    --frame: #ffffff;
    --petal: #f0d21c;
    --leaf-dark: #3f4638;
    --leaf-mid: #6c7460;
  }
  html, body {
    margin: 0;
    padding: 0;
    width: 873px;
    height: 1200px;
    overflow: hidden;
    background: var(--sky);
  }
  .cover {
    position: relative;
    width: 873px;
    height: 1200px;
    background: var(--sky);
    font-family: "Open Sans", Arial, sans-serif;
  }
  .title-block {
    position: absolute;
    left: 0;
    top: 0;
    width: 873px;
    height: 360px;
  }
  .title-main {
    font-family: "Open Sans", Arial, sans-serif;
    font-weight: 800;
    fill: var(--title-blue);
  }
  .title-band {
    fill: var(--band);
  }
  .title-script {
    font-family: "Dancing Script", cursive;
    font-weight: 600;
    fill: #ffffff;
  }
  .title-sub {
    font-family: "Open Sans", Arial, sans-serif;
    font-weight: 700;
    fill: var(--title-blue);
  }
  .photo-grid {
    position: absolute;
    left: 87px;
    top: 377px;
    width: 713px;
    height: 663px;
    box-sizing: border-box;
    padding: 8px;
    background: var(--frame);
    display: grid;
    grid-template-columns: repeat(3, 1fr);
    grid-template-rows: repeat(3, 1fr);
    gap: 2px;
  }
  .photo {
    background: radial-gradient(circle at 50% 48%, var(--petal) 0 26%, #d9bb1a 34%, var(--leaf-mid) 52%, var(--leaf-dark) 100%);
  }
  .photo--daisy {
    background: radial-gradient(circle at 50% 48%, #e59b1e 0 9%, var(--petal) 14% 30%, #d4b51b 38%, var(--leaf-mid) 56%, #5a5a52 100%);
  }
  .author {
    position: absolute;
    left: 0;
    top: 1064px;
    width: 873px;
    margin: 0;
    text-align: center;
    font-family: "Open Sans", Arial, sans-serif;
    font-weight: 400;
    font-size: 54px;
    line-height: 1.2;
    color: var(--title-blue);
  }
</style>
</head>
<body>
<main class="cover">
  <svg class="title-block" viewBox="0 0 873 360" width="873" height="360" aria-label="Bloom Guide Beside the path Southern Arizona Desert">
    <text class="title-main" x="86" y="166" font-size="92" textLength="702" lengthAdjust="spacing">BLOOM GUIDE</text>
    <rect class="title-band" x="86" y="190" width="702" height="90"/>
    <text class="title-script" x="437" y="255" font-size="68" text-anchor="middle">Beside the path</text>
    <text class="title-sub" x="86" y="338" font-size="48" textLength="702" lengthAdjust="spacing">Southern Arizona Desert</text>
  </svg>

  <section class="photo-grid">
    <div class="photo" role="img" aria-label="Photo of a yellow four-petaled desert flower with red centre"></div>
    <div class="photo" role="img" aria-label="Photo of a yellow four-petaled flower on a hairy stem"></div>
    <div class="photo" role="img" aria-label="Photo of a pale yellow primrose-like flower"></div>
    <div class="photo" role="img" aria-label="Photo of a yellow five-petaled flower with bud"></div>
    <div class="photo" role="img" aria-label="Photo of a small yellow five-petaled flower among stems"></div>
    <div class="photo" role="img" aria-label="Photo of a yellow flower with widely spaced petals"></div>
    <div class="photo photo--daisy" role="img" aria-label="Photo of a yellow daisy-like flower"></div>
    <div class="photo photo--daisy" role="img" aria-label="Photo of a yellow daisy with orange centre on grey leaves"></div>
    <div class="photo photo--daisy" role="img" aria-label="Photo of a narrow-rayed yellow daisy"></div>
  </section>

  <p class="author">Daniel Brekken</p>
</main>
</body>
</html>
```